Utility Software Company Needs a Business Flyer

We need a business flyer to promote one of our Services. The MBA Department is a Service within our company and it is basically Managed Backoffice Administration. MBA provides services that lighten the workload for our clients. MBA has a team of professionals who specialize in data processing, bill processing, research, customer support, and security of financial data. We remove the burden of in house billing and payment processing.

Target Market(s)

New and existing utility customers

Industry/Entity Type

Public Utility

Font styles to use
Serif

Colors
ffcf3e
3277b5
85cae6

Requirements
Must have
• The company name - KLT, Inc.
• Logo
• Tagline
• Address - 48710 Brimley Lane, Houston, TX 77093
• Phone: 713-846-2059
• Email: sales@kltzo.com
• Website - www.kltzo.com
• Contact a Sales Associate for more information
• Diverse images of people

```html
<!DOCTYPE html>
<html lang="en">
<head>
<meta charset="utf-8">
<title>KLT, Inc. – SBD Flyer</title>
<link href="https://fonts.googleapis.com/css2?family=Jost:wght@300;400;500;600;700&display=swap" rel="stylesheet">
<style>
:root{
  --blue:#3277b5;
  --blue-deep:#1f5a9c;
  --sky:#85cae6;
  --yellow:#ffcf3e;
  --ink:#3a3a3a;
  --bg:#e9e6e1;
  --white:#ffffff;
}
*{margin:0;padding:0;box-sizing:border-box}
html,body{width:977px;height:1200px;overflow:hidden;background:var(--bg);font-family:'Jost',sans-serif;color:var(--ink)}
.spread{position:absolute;top:267px;left:11px;display:flex;gap:15px}
.page{position:relative;width:470px;height:665px;background:var(--white);overflow:hidden;box-shadow:0 4px 14px rgba(0,0,0,.18)}
.layer{position:absolute;left:0;top:0}
.brand{position:absolute;top:12px;display:flex;align-items:center;gap:6px;color:var(--white);font-weight:600;font-size:15px;letter-spacing:.2px;white-space:nowrap}
.brand-dot{width:14px;height:14px;border-radius:50%;background:var(--white)}
.brand-since{position:absolute;top:31px;font-size:5px;color:var(--white)}
.photo{position:absolute;left:0;top:40px;width:470px;height:320px;background:linear-gradient(135deg,#2c4d63 0%,#5e8ea3 45%,#c9d5d7 75%,#8a9ba3 100%)}
.badge{position:absolute;border-radius:50%;border:3px solid var(--white);box-shadow:0 1px 4px rgba(0,0,0,.3)}
.title{position:absolute;left:0;width:470px;top:372px;text-align:center;color:var(--blue);font-weight:700;font-size:22.5px;letter-spacing:.2px}
.subtitle{position:absolute;left:0;width:470px;top:402px;text-align:center;color:#666;font-weight:300;font-size:12.5px;line-height:1.2}
.body-copy{position:absolute;left:22px;right:22px;top:426px;font-size:7.4px;line-height:1.38;text-align:justify}
.body-copy p{margin-bottom:7px}
.tollfree{position:absolute;left:180px;top:562px;width:110px;text-align:center}
.tollfree-label{font-size:7px;color:#666}
.tollfree-num{border:1px solid var(--blue);color:var(--blue);font-weight:600;font-size:12px;padding:1px 0}
.email{position:absolute;left:12px;top:622px;font-size:8px;color:var(--blue);display:flex;align-items:center;gap:3px}
.address{position:absolute;left:170px;top:630px;font-size:8.5px;color:var(--white);line-height:1.3;display:flex;gap:6px;align-items:center}
.contact{position:absolute;left:300px;top:620px;color:var(--white);border-left:1px solid var(--white);padding-left:8px}
.contact-row{display:flex;align-items:center;gap:6px}
.phone{font-size:17px;font-weight:600}
.web{font-size:14px}
.web b{color:var(--yellow);font-weight:600}
.services{position:absolute;left:18px;top:60px;color:var(--blue)}
.services-kicker{font-size:20px;font-weight:300;line-height:1}
.services-head{font-size:22px;font-weight:700;line-height:1.1}
.services-lead{font-size:14px;color:#444;font-weight:300}
.tab{position:absolute;left:0;height:22px;display:flex;align-items:center;padding-left:18px;color:var(--white);font-size:17px;font-weight:300}
.tab svg{position:absolute;left:0;top:0;z-index:0}
.tab span{position:relative;z-index:1}
.tab-small{font-size:10.5px;font-weight:600;height:18px}
.note{position:absolute;left:28px;right:22px;font-size:7px;line-height:1.35}
.list{position:absolute;left:28px;right:18px;font-size:7px;line-height:1.35;list-style:none}
.list li{position:relative;padding-left:12px;margin-bottom:7px}
.list li::before{content:"";position:absolute;left:0;top:3px;width:3px;height:3px;border-radius:50%;background:var(--blue)}
.list b{color:var(--blue);font-weight:600}
.panel{position:absolute;left:0;top:326px;width:470px;height:120px;background:var(--blue)}
.panel .list{color:var(--white);top:10px}
.panel .list b{color:var(--white)}
.panel .list li::before{background:var(--white)}
.adv li{margin-bottom:5px}
.checks{list-style:none;margin-top:2px}
.checks li{padding-left:12px;margin-bottom:1px}
.checks li::before{content:"✓";background:none;width:auto;height:auto;top:0;font-size:7px;color:var(--blue)}
</style>
</head>
<body>
<div class="spread">

  <section class="page page-front">
    <div class="photo" role="img" aria-label="Photo of two colleagues reviewing data on computer monitors in an office"></div>
    <svg class="layer" width="470" height="665" viewBox="0 0 470 665">
      <polygon points="0,0 470,0 470,38 290,92 0,36" fill="var(--blue)"/>
      <polygon points="0,36 290,92 470,38 470,44 290,100 0,42" fill="var(--white)"/>
      <polygon points="0,42 290,100 470,44 470,52 290,108 0,50" fill="var(--yellow)"/>
      <polygon points="0,322 250,352 470,306 470,314 250,362 0,330" fill="var(--blue)"/>
      <polygon points="0,330 250,362 470,314 470,665 0,665" fill="var(--white)"/>
      <polygon points="0,578 0,665 95,665" fill="var(--yellow)"/>
      <polygon points="0,665 0,658 470,586 470,665" fill="var(--blue-deep)"/>
      <polygon points="150,620 470,574 470,586 170,630" fill="var(--yellow)"/>
    </svg>
    <div class="brand" style="left:30px"><span class="brand-dot"></span>KLT, Inc. &nbsp;Trusted Utility Partners</div>
    <div class="brand-since" style="left:262px">Est. 1991</div>
    <div class="badge" style="left:192px;top:285px;width:62px;height:62px;background:linear-gradient(135deg,#6fa6c9,#dfe9ee)" role="img" aria-label="Photo of a hand holding a phone showing a payment app"></div>
    <div class="badge" style="left:272px;top:270px;width:82px;height:82px;background:linear-gradient(135deg,#7f8a94,#d7d2cc)" role="img" aria-label="Photo of a smiling office representative"></div>
    <div class="badge" style="left:380px;top:246px;width:84px;height:84px;background:linear-gradient(135deg,#2e6fb0,#9fd0ec)" role="img" aria-label="Illustration of a business professional with a software product emblem"></div>

    <h1 class="title">DATA PROCESSING &amp; BILL PROCESSING</h1>
    <p class="subtitle">Shared Billing Desk, Services That Lighten Your Work Load</p>
    <div class="body-copy">
      <p>The KLT Shared Billing Desk (SBD) is here to help you manage your business effectively by systematically organizing your data and information from diverse sources, allowing you and your staff/teams to spend more time serving your customers. We convert, enter, manage, evaluate and process your data based on the individual municipality rate ordinance or per your requirement(s). With a wide range of services, we have helped companies streamline their back office and manage work more efficiently. You can rely on our extensive industry knowledge and flexible services that are cost-effective and productive.</p>
      <p>We have an efficient and experienced team working with a vast understanding of the various tasks involved in completing the entire billing cycle. All our representatives are friendly and knowledgeable. KLT will methodically maintain all the records and data for you, conducting processes for better client and customer relationships, bringing you maximum value.</p>
      <p>We provide you with total transparency of data. If required, we inter-connect your data so that it is easily available to your staff immediately, making interacting with customers more convenient.</p>
    </div>
    <div class="tollfree">
      <div class="tollfree-label">Toll Free Number</div>
      <div class="tollfree-num">1-855-430-2917</div>
    </div>
    <div class="email">
      <svg width="10" height="10" viewBox="0 0 10 10"><circle cx="5" cy="5" r="4.5" fill="var(--blue)"/><rect x="2.5" y="3.3" width="5" height="3.4" fill="none" stroke="var(--white)" stroke-width=".7"/></svg>
      sales@kltzo.com
    </div>
    <div class="address">
      <svg width="10" height="13" viewBox="0 0 10 13"><path d="M5 12 C2 8 1 6 1 4.5 A4 4 0 0 1 9 4.5 C9 6 8 8 5 12Z" fill="none" stroke="var(--yellow)" stroke-width="1.2"/><circle cx="5" cy="4.5" r="1.4" fill="var(--yellow)"/></svg>
      <span>48710 Brimley Lane,<br>Houston, TX 77093</span>
    </div>
    <div class="contact">
      <div class="contact-row">
        <svg width="14" height="14" viewBox="0 0 14 14"><path d="M3 1 L5.5 3.5 L4 5.5 C5 7.5 6.5 9 8.5 10 L10.5 8.5 L13 11 L11 13 C6 12 2 8 1 3Z" fill="var(--yellow)"/></svg>
        <span class="phone">713-846-2059</span>
      </div>
      <div class="contact-row">
        <svg width="14" height="14" viewBox="0 0 14 14"><circle cx="7" cy="7" r="6" fill="none" stroke="var(--yellow)" stroke-width="1.2"/><ellipse cx="7" cy="7" rx="2.6" ry="6" fill="none" stroke="var(--yellow)" stroke-width="1"/><line x1="1" y1="7" x2="13" y2="7" stroke="var(--yellow)" stroke-width="1"/></svg>
        <span class="web">www.<b>kltzo</b>.com</span>
      </div>
    </div>
  </section>

  <section class="page page-services">
    <svg class="layer" width="470" height="665" viewBox="0 0 470 665">
      <polygon points="0,0 470,0 470,36 360,70 0,30" fill="var(--blue)"/>
      <polygon points="0,30 360,70 470,36 470,42 360,78 0,34" fill="var(--white)"/>
      <polygon points="0,34 360,78 470,42 470,50 360,88 0,39" fill="var(--yellow)"/>
      <polygon points="0,665 0,656 470,610 470,665" fill="var(--blue)"/>
      <polygon points="120,665 470,626 470,634 200,665" fill="var(--yellow)"/>
    </svg>
    <div class="brand" style="left:218px"><span class="brand-dot"></span>KLT, Inc. &nbsp;Trusted Utility Partners</div>
    <div class="brand-since" style="left:430px">Est. 1991</div>

    <div class="services">
      <div class="services-kicker">SERVICES</div>
      <div class="services-head">SBD PROVIDES:</div>
      <div class="services-lead">Payment channels that SBD processes:</div>
    </div>

    <div class="tab" style="top:128px;width:150px">
      <svg width="150" height="22" viewBox="0 0 150 22"><polygon points="0,0 128,0 140,22 0,22" fill="var(--blue)"/><polygon points="131,0 138,0 150,22 143,22" fill="var(--yellow)"/></svg>
      <span>eScan</span>
    </div>
    <p class="note" style="top:155px">Lock Box – Payments that are mailed to a secure mail box and processed in the SBD office daily Monday – Friday.<br>All payments received each day are processed the same day.</p>

    <div class="tab" style="top:180px;width:210px">
      <svg width="210" height="22" viewBox="0 0 210 22"><polygon points="0,0 188,0 200,22 0,22" fill="var(--blue)"/><polygon points="191,0 198,0 210,22 203,22" fill="var(--yellow)"/></svg>
      <span>Online Payments</span>
    </div>
    <ul class="list" style="top:210px">
      <li><b>SwiftPay –</b> Payments made using the QR Code on the customer's billing statement which allows the customer to retrieve payment information regarding their account and to make payments in a few effortless steps.</li>
      <li><b>Batch Files –</b> Payments that are made online using the billing portal/website or via telephone which can be made by check or credit card/debit card payments.</li>
      <li><b>eReceivables –</b> Payments that are made by a customer using online banking or payments made at one of their local payment outlets that accepts utility payments, such as Mercado Plus, FreshWay, Lone Star Grocer etc.</li>
      <li><b>Recurring ACH/Credit Cards –</b> Customers that sign up for this service will have funds drafted from their bank account or applied to their credit card each month based on their current balance and they will not have to worry about manually making payments each month or forgetting to make a payment.</li>
    </ul>

    <div class="panel">
      <ul class="list">
        <li><b>Billing –</b> SBD will process billing statements each month based on the guidance of the operator. Bills are automatically calculated based on meter reads and the rate ordinance that was provided by the operator for each of its districts.</li>
        <li><b>Secured file storage of payments –</b> Every payment that is processed by SBD is stored electronically for a minimum of 2 years and can be accessed for clients upon written request.</li>
        <li><b>Research –</b> SBD provides general to complex research of payments, discrepancies, etc.</li>
        <li><b>Support –</b> SBD provides general support for our clients and if SBD cannot immediately resolve an issue that issue will be escalated to the next higher support level for resolution.</li>
      </ul>
    </div>

    <div class="tab tab-small" style="top:456px;width:200px">
      <svg width="200" height="18" viewBox="0 0 200 18"><polygon points="0,0 178,0 188,18 0,18" fill="var(--blue)"/><polygon points="181,0 188,0 198,18 191,18" fill="var(--yellow)"/></svg>
      <span>Advantages of using SBD</span>
    </div>
    <ul class="list adv" style="top:482px">
      <li>No learning curves to learn software. Payments and billing will be up and running immediately after conversion.</li>
      <li>Actual staff personnel to talk to when you have an issue.</li>
      <li>We have an efficient and experienced team working with a vast understanding of the various tasks involved in finalizing the billing cycle.</li>
      <li>Generally, more cost effective than processing payments and billing in-house.</li>
      <li>Deposits are usually made faster when using the SBD department versus using in-house processors.</li>
      <li>Assistance with delinquent letters and tags if requested.</li>
      <li>Reports to help balance bank statements.
        <ul class="checks">
          <li>To make sure that the amount expected to be processed was processed.</li>
          <li>What was expected to go to the bank is what went to the bank.</li>
          <li>And that the bank received each payment.</li>
        </ul>
      </li>
      <li>Can provide customizable services depending on our client's needs.</li>
    </ul>
  </section>

</div>
</body>
</html>
```